Corporate Letterhead

Looking for a new corporate letterhead design. Our colors are orange and gray.

We'd like it if the below could be included somehow in the letterhead.                                       

Partnerships | Results | Quality

• Logo, Company Name, Address, Phone #, Fax #, Web address, Email address (optional), the phrase "A Service Disable Veteran Owned Small Business".

```html
<!DOCTYPE html>
<html lang="en">
<head>
<meta charset="utf-8">
<title>Oventra Technology Inc. – Letterhead</title>
<link rel="stylesheet" href="https://fonts.googleapis.com/css2?family=Michroma&family=Arimo:wght@400&display=swap">
<style>
  :root {
    --orange: #f28c1c;
    --gray: #8a8a8a;
    --gray-dark: #555555;
    --text: #333333;
    --swirl: #e6e6e6;
    --paper: #ffffff;
    --backdrop: #dcdcdc;
  }
  * { box-sizing: border-box; margin: 0; padding: 0; }
  html, body { width: 1200px; height: 847px; overflow: hidden; }
  body { background: var(--backdrop); font-family: "Arimo", Arial, sans-serif; }

  .letterhead {
    position: absolute; left: 272px; top: 0;
    width: 655px; height: 847px;
    background: var(--paper); overflow: hidden;
  }
  .accent-bar { position: absolute; width: 6px; background: var(--orange); }

  .tagline { position: absolute; left: 50px; top: 50px; }
  .tagline .accent-bar { left: 0; top: 0; height: 44px; }
  .tagline ul {
    list-style: none; margin-left: 16px;
    font-family: "Michroma", sans-serif; font-size: 9px; line-height: 14px;
    color: var(--gray); letter-spacing: 0.5px;
  }

  .brand {
    position: absolute; right: 48px; top: 54px;
    display: flex; align-items: center; gap: 10px;
  }
  .brand-dot { width: 26px; height: 26px; border-radius: 50%; background: var(--orange); }
  .brand-name {
    font-family: "Michroma", sans-serif; font-size: 16px;
    color: var(--orange); letter-spacing: 0.5px;
  }

  .decor-circle {
    position: absolute; right: -150px; top: 470px;
    width: 460px; height: 460px; border-radius: 50%;
    background: var(--swirl); opacity: 0.55;
  }

  .letter-body {
    position: absolute; left: 60px; top: 130px; width: 540px;
    font-size: 9.5px; line-height: 15px; color: var(--text);
  }
  .salutation { margin-bottom: 12px; }
  .letter-body p.copy { text-align: justify; margin-bottom: 15px; padding-left: 14px; }

  .signature { position: absolute; left: 450px; top: 575px; width: 150px; }
  .signature-mark {
    width: 130px; height: 34px; margin-bottom: 6px;
    background: linear-gradient(90deg, rgba(40,40,40,0.12), rgba(40,40,40,0.04));
    border-radius: 4px;
  }
  .signature p { font-size: 9.5px; line-height: 13px; color: var(--text); padding-left: 14px; }

  .footer { position: absolute; left: 50px; top: 750px; width: 560px; }
  .footer .accent-bar { left: 0; top: 0; height: 62px; }
  .footer-inner { margin-left: 16px; font-family: "Michroma", sans-serif; }
  .company-name { font-size: 11px; color: var(--orange); letter-spacing: 0.5px; line-height: 15px; }
  .address { font-size: 9.5px; color: var(--gray-dark); line-height: 15px; margin-bottom: 6px; }
  .contact { display: flex; font-size: 8.5px; line-height: 12px; color: var(--gray-dark); }
  .contact-col { padding-right: 12px; }
  .contact-col + .contact-col { border-left: 1px solid var(--gray); padding-left: 8px; }
  .contact .label { color: var(--orange); }
</style>
</head>
<body>
  <article class="letterhead">
    <div class="decor-circle" aria-hidden="true"></div>

    <header>
      <div class="tagline">
        <span class="accent-bar"></span>
        <ul>
          <li>PARTNERSHIPS</li>
          <li>RESULTS</li>
          <li>QUALITY</li>
        </ul>
      </div>
      <div class="brand">
        <span class="brand-dot"></span>
        <span class="brand-name">OVENTRA TECHNOLOGY INC</span>
      </div>
    </header>

    <main class="letter-body">
      <p class="salutation">Dear Client,</p>
      <p class="copy">Lorem ipsum dolor sit amet, consectetur adipisicing elit, sed do eiusmod tempor incididunt ut labore et dolore magna aliqua. Ut enim ad minim veniam, quis nostrud exercitation ullamco laboris nisi ut aliquip ex ea commodo consequat. Duis aute irure dolor in reprehenderit in voluptate velit esse cillum dolore eu fugiat nulla pariatur. Excepteur sint occaecat cupidatat non proident, sunt in culpa qui officia deserunt mollit anim id est laborum.</p>
      <p class="copy">Lorem ipsum dolor sit amet, consectetur adipisicing elit, sed do eiusmod tempor incididunt ut labore et dolore magna aliqua. Ut enim ad minim veniam, quis nostrud exercitation ullamco laboris nisi ut aliquip ex ea commodo consequat. Duis aute irure dolor in reprehenderit in voluptate velit esse cillum dolore eu fugiat nulla pariatur. Excepteur sint occaecat cupidatat non proident, sunt in culpa qui officia deserunt mollit anim id est laborum.</p>
      <p class="copy">Lorem ipsum dolor sit amet, consectetur adipisicing elit, sed do eiusmod tempor incididunt ut labore et dolore magna aliqua. Ut enim ad minim veniam, quis nostrud exercitation ullamco laboris nisi ut aliquip ex ea commodo consequat. Duis aute irure dolor in reprehenderit in voluptate velit esse cillum dolore eu fugiat nulla pariatur. Excepteur sint occaecat cupidatat non proident, sunt in culpa qui officia deserunt mollit anim id est laborum.</p>
      <p class="copy">Lorem ipsum dolor sit amet, consectetur adipisicing elit, sed do eiusmod tempor incididunt ut labore et dolore magna aliqua. Ut enim ad minim veniam, quis nostrud exercitation ullamco laboris nisi ut aliquip ex ea commodo consequat. Duis aute irure dolor in reprehenderit in voluptate velit esse cillum dolore eu fugiat nulla pariatur. Excepteur sint occaecat cupidatat non proident, sunt in culpa qui officia deserunt mollit anim id est laborum.</p>
      <p class="copy">Lorem ipsum dolor sit amet, consectetur adipisicing elit, sed do eiusmod tempor incididunt ut labore et dolore magna aliqua. Ut enim ad minim veniam, quis nostrud exercitation ullamco laboris nisi ut aliquip ex ea.</p>
    </main>

    <div class="signature">
      <div class="signature-mark" role="img" aria-label="Handwritten signature of Mark Ellison"></div>
      <p>Mark Ellison<br>Executive manager</p>
    </div>

    <footer class="footer">
      <span class="accent-bar"></span>
      <div class="footer-inner">
        <p class="company-name">OVENTRA TECHNOLOGY INC.</p>
        <p class="address">1420 COMMERCE DRIVE | SUITE 210 | GLENMORE, MD 21000</p>
        <div class="contact">
          <div class="contact-col">
            <p><span class="label">P:</span> 555.013.4470</p>
            <p><span class="label">F:</span> 555.017.3392</p>
          </div>
          <div class="contact-col">
            <p>INFO@OVENTRATECHINC.COM</p>
            <p>WWW.OVENTRATECHINC.COM</p>
          </div>
        </div>
      </div>
    </footer>
  </article>
</body>
</html>
```